Business Cards for Financial Service Consulting Business Ltd

Business Card Design for my risk management consultancy to the financial service industry
Responsible Lending, Fair Charges, Ethical Collections

Should be serious, professional, corporate

Target Market(s)

Fintech, Financial Services Industry

Industry/Entity Type

Financial Service

Contact Information for Business Card

Lewis Marsh
lew@slatewellconsulting.co.uk
07931520478
01632960417

Font styles to use
Serif

Colors

Designer to choose colors to be used in the design.

Requirements
Must have
• Name: Slatewell Consulting
• Logo, contact details
• The three pillars of my business Responsible Lending, Fair Charges, Ethical Collections
Nice to have
• Corporate Feel
Should not have
• jokes, pretty pictures, cartoons

```html
<!DOCTYPE html>
<html lang="en">
<head>
<meta charset="utf-8">
<title>Slatewell Consulting — Business Cards</title>
<link rel="stylesheet" href="https://fonts.googleapis.com/css2?family=Raleway:wght@400;500;600;700&display=swap">
<style>
  :root {
    --backdrop: #d4d4d2;
    --brand-blue: #0a6c9f;
    --brand-blue-light: #0a88b6;
    --cream: #ece5cd;
    --cream-text: #f3eddb;
    --ink-blue: #17689a;
  }
  * { margin: 0; padding: 0; box-sizing: border-box; }
  html, body {
    width: 1200px;
    height: 905px;
    overflow: hidden;
    background: var(--backdrop);
    font-family: "Raleway", sans-serif;
  }
  .canvas {
    position: relative;
    width: 1200px;
    height: 905px;
  }
  .card { position: absolute; overflow: hidden; }

  /* Front of card */
  .card-front {
    left: 48px; top: 14px;
    width: 792px; height: 452px;
    background: var(--brand-blue);
    z-index: 2;
  }
  .front-block {
    position: absolute;
    left: 0; top: 172px;
    width: 326px; height: 280px;
    background: var(--brand-blue-light);
  }
  .wordmark {
    position: absolute;
    left: 84px; top: 122px;
    font-size: 42px;
    font-weight: 500;
    letter-spacing: 0.12em;
    color: var(--cream-text);
    white-space: nowrap;
    line-height: 1;
  }
  .pillars {
    position: absolute;
    left: 350px; top: 298px;
    list-style: none;
  }
  .pillars li {
    font-size: 21px;
    font-weight: 700;
    letter-spacing: 0.2em;
    color: var(--cream-text);
    line-height: 38px;
  }

  /* Back of card */
  .card-back {
    left: 372px; top: 440px;
    width: 786px; height: 448px;
    background: var(--cream);
    z-index: 1;
    color: var(--ink-blue);
    text-align: center;
  }
  .brand-square {
    position: absolute;
    left: 374px; top: 88px;
    width: 40px; height: 40px;
    background: var(--brand-blue-light);
  }
  .person-name {
    position: absolute;
    left: 0; right: 0; top: 176px;
    font-size: 32px;
    font-weight: 700;
    letter-spacing: 0.55em;
    padding-left: 0.55em;
  }
  .email {
    position: absolute;
    left: 0; right: 0; top: 224px;
    font-size: 20px;
    font-weight: 400;
    letter-spacing: 0.13em;
  }
  .phones {
    position: absolute;
    left: 0; right: 0; top: 286px;
    list-style: none;
  }
  .phones li {
    font-size: 29px;
    font-weight: 700;
    letter-spacing: 0.08em;
    line-height: 38px;
  }
</style>
</head>
<body>
<main class="canvas">
  <section class="card card-front" aria-label="Card front">
    <div class="front-block"></div>
    <h1 class="wordmark">SLATEWELL CONSULTING</h1>
    <ul class="pillars">
      <li>RESPONSIBLE LENDING</li>
      <li>FAIR CHARGES</li>
      <li>ETHICAL COLLECTIONS</li>
    </ul>
  </section>

  <section class="card card-back" aria-label="Card back">
    <div class="brand-square"></div>
    <h2 class="person-name">LEWIS MARSH</h2>
    <p class="email">LEW@SLATEWELLCONSULTING.CO.UK</p>
    <ul class="phones">
      <li>07931520478</li>
      <li>01632960417</li>
    </ul>
  </section>
</main>
</body>
</html>
```